The Marrows 100% real ingredients

I need a label design for my hummus.
"The Lark" Hummus
Roasted Red Pepper hummus infused with Crushed Red Pepper for a kick
Made With Real Ingredients
Oil Free
Preservative Free
in small print: TheMarrowsNaturalFoods.com
I also need an ingredient list
Chickpeas, Tahini, Red bell pepper, Sweet onion, Garlic, Water, Lemon, Maple syrup, Crushed red pepper, Pink Himalayan salt, Cumin, Cayenne, Black pepper,Baking soda
In our Hummus:
We believe that our hummus doesn't need all the extra ingredients like oils and preservatives. We want you to feel good after eating our products while also eating good food that is good for you! So we use fresh ingredients like lemon, garlic, red peppers, and sweet onions.
In the design can you put a red roasted pepper in the background?
Two of the pictures I uploaded are examples of what I would like it to look like.

```html
<!DOCTYPE html>
<html lang="en">
<head>
<meta charset="utf-8">
<title>The Lark Hummus – Label Set</title>
<link rel="stylesheet" href="https://fonts.googleapis.com/css2?family=Barlow:wght@400;500&family=Kaushan+Script&family=Montserrat:wght@500&family=Playfair+Display:wght@700;900&display=swap">
<style>
  :root{
    --red:#ad1218;
    --black:#0d0d0d;
    --white:#ffffff;
    --board:#f1f1f1;
    --board-dark:#e2e2e2;
    --ink:#1a1a1a;
    --grey:#6f6f6f;
    --pepper:#d8301c;
    --pepper-dark:#8e1a10;
    --plate:#f7f7f7;
    --rule:#222;
  }
  *{margin:0;padding:0;box-sizing:border-box}
  html,body{width:1200px;height:906px;overflow:hidden;background:var(--white)}
  .canvas{position:relative;width:1200px;height:906px;background:var(--white)}

  /* dimension callouts */
  .dim{position:absolute;font-family:"Montserrat",sans-serif;font-weight:500;font-size:16px;color:var(--ink)}
  .dim-line{position:absolute;background:var(--rule)}
  .dim-v-text{transform:translate(-50%,-50%) rotate(-90deg);white-space:nowrap}

  /* label shell */
  .label{position:absolute;overflow:hidden;border-radius:16px;
    background:linear-gradient(180deg,var(--board) 0%,var(--white) 18%,var(--board) 34%,var(--white) 52%,var(--board) 70%,var(--white) 86%,var(--board-dark) 100%);}
  .label > *{position:absolute}
  .pepper-photo{background:radial-gradient(circle at 62% 38%,var(--pepper) 0%,var(--pepper) 34%,var(--pepper-dark) 50%,var(--plate) 58%,var(--plate) 78%,var(--board-dark) 100%)}

  .brand-seal{display:flex;align-items:center;justify-content:center;border:1.5px solid var(--ink);border-radius:50%;
    font-family:"Playfair Display",serif;font-weight:700;color:var(--ink);white-space:nowrap}
  .script{font-family:"Kaushan Script",cursive;color:var(--red);white-space:nowrap}
  .product-name{font-family:"Playfair Display",serif;font-weight:900;color:var(--black);white-space:nowrap}
  .product-desc{font-family:"Playfair Display",serif;font-weight:700;color:var(--grey)}
  .claim{display:flex;flex-direction:column;align-items:center;font-family:"Barlow",sans-serif;font-weight:500;color:var(--white);text-align:center;line-height:1.1}
  .claim svg{display:block}
  .net-weight{font-family:"Playfair Display",serif;font-weight:700;color:var(--white);white-space:nowrap}
  .web{font-family:"Playfair Display",serif;font-weight:700;color:var(--white);white-space:nowrap}
  .body-copy{font-family:"Barlow",sans-serif;font-weight:400;color:var(--ink)}

  /* front small */
  .front-small{left:146px;top:129px;width:327px;height:261px}
  .front-small .sidebar{left:0;top:0;width:79px;height:190px;background:var(--red)}
  .front-small .weight-box{left:0;top:190px;width:79px;height:71px;background:var(--black)}
  .front-small .claim{left:0;width:79px;font-size:10px}
  .front-small .net-weight{left:0;width:79px;text-align:center;top:200px;font-size:11px;line-height:1.1}
  .front-small .net-weight b{display:block;font-size:20px}

  /* back */
  .back{left:146px;top:519px;width:327px;height:262px}
  .back .footer{left:0;bottom:0;width:100%;height:41px;background:var(--red);display:flex;align-items:center;justify-content:center}

  /* front large */
  .front-large{left:633px;top:248px;width:457px;height:457px}
  .front-large .band{left:0;top:364px;width:100%;height:93px;background:var(--red)}
  .front-large .claim{font-size:12px}
</style>
</head>
<body>
<svg width="0" height="0" style="position:absolute">
  <symbol id="icon-oil-free" viewBox="0 0 44 44">
    <circle cx="22" cy="22" r="20" fill="none" stroke="#fff" stroke-width="2.4"/>
    <path d="M22 9 C17 17 13 21 13 26 a9 9 0 0 0 18 0 C31 21 27 17 22 9Z" fill="#fff"/>
    <path d="M18 24 a5 5 0 0 0 3 7" fill="none" stroke="#ad1218" stroke-width="2"/>
    <line x1="8" y1="8" x2="36" y2="36" stroke="#fff" stroke-width="3"/>
    <line x1="9.5" y1="9.5" x2="34.5" y2="34.5" stroke="#ad1218" stroke-width="1" transform="translate(1.5,-1.5)"/>
  </symbol>
  <symbol id="icon-preservative-free" viewBox="0 0 44 44">
    <circle cx="22" cy="22" r="20" fill="none" stroke="#fff" stroke-width="2.4"/>
    <path d="M19 13 h6 M20 13 v7 l-7 12 h18 l-7-12 v-7" fill="none" stroke="#fff" stroke-width="2"/>
    <path d="M16 28 h12 l2 4 h-16Z" fill="#fff"/>
    <circle cx="22" cy="9" r="1.2" fill="#fff"/><circle cx="24" cy="6" r="0.9" fill="#fff"/>
    <line x1="8" y1="8" x2="36" y2="36" stroke="#fff" stroke-width="3"/>
  </symbol>
</svg>

<main class="canvas">

  <!-- dimensions: front small -->
  <div class="dim-line" style="left:146px;top:107px;width:327px;height:1px"></div>
  <div class="dim-line" style="left:146px;top:94px;width:1px;height:25px"></div>
  <div class="dim-line" style="left:472px;top:94px;width:1px;height:25px"></div>
  <div class="dim" style="left:290px;top:78px">2.5 in.</div>
  <div class="dim-line" style="left:119px;top:129px;width:1px;height:261px"></div>
  <div class="dim-line" style="left:106px;top:129px;width:26px;height:1px"></div>
  <div class="dim-line" style="left:106px;top:389px;width:26px;height:1px"></div>
  <div class="dim dim-v-text" style="left:103px;top:252px">2 in.</div>

  <!-- dimensions: back -->
  <div class="dim-line" style="left:146px;top:497px;width:327px;height:1px"></div>
  <div class="dim-line" style="left:146px;top:484px;width:1px;height:25px"></div>
  <div class="dim-line" style="left:472px;top:484px;width:1px;height:25px"></div>
  <div class="dim" style="left:290px;top:469px">2.5 in.</div>
  <div class="dim-line" style="left:119px;top:519px;width:1px;height:262px"></div>
  <div class="dim-line" style="left:106px;top:519px;width:26px;height:1px"></div>
  <div class="dim-line" style="left:106px;top:780px;width:26px;height:1px"></div>
  <div class="dim dim-v-text" style="left:103px;top:643px">2 in.</div>

  <!-- dimensions: front large -->
  <div class="dim-line" style="left:633px;top:217px;width:457px;height:1px"></div>
  <div class="dim-line" style="left:633px;top:204px;width:1px;height:25px"></div>
  <div class="dim-line" style="left:1089px;top:204px;width:1px;height:25px"></div>
  <div class="dim" style="left:838px;top:188px">3.5 in.</div>
  <div class="dim-line" style="left:602px;top:248px;width:1px;height:457px"></div>
  <div class="dim-line" style="left:590px;top:248px;width:25px;height:1px"></div>
  <div class="dim-line" style="left:590px;top:704px;width:25px;height:1px"></div>
  <div class="dim dim-v-text" style="left:584px;top:458px">3.5 in.</div>

  <!-- front label, small -->
  <section class="label front-small">
    <div class="sidebar"></div>
    <div class="weight-box"></div>
    <div class="claim" style="top:36px"><svg width="38" height="38"><use href="#icon-oil-free"/></svg><span style="margin-top:3px">Oil free</span></div>
    <div class="claim" style="top:105px"><svg width="38" height="38"><use href="#icon-preservative-free"/></svg><span style="margin-top:3px">Preservative<br>free</span></div>
    <div class="net-weight">Net Wt.:<b>12 oz</b></div>
    <div class="pepper-photo" role="img" aria-label="Roasted red peppers on a white plate" style="left:214px;top:0;width:113px;height:127px"></div>
    <div class="brand-seal" style="left:94px;top:28px;width:110px;height:110px;font-size:14px">The Marrows</div>
    <div class="script" style="left:206px;top:115px;font-size:16px;line-height:1.05;transform:rotate(-4deg)">Made with<br>real ingredients</div>
    <h1 class="product-name" style="left:93px;top:163px;font-size:22px">The Lark Hummus</h1>
    <p class="product-desc" style="left:93px;top:193px;width:225px;font-size:13.5px;line-height:14.6px">Roasted Red Pepper hummus infused with Crushed Red Pepper for a kick</p>
  </section>

  <!-- back label -->
  <section class="label back">
    <div class="pepper-photo" role="img" aria-label="Roasted red peppers on a white plate" style="left:214px;top:0;width:113px;height:130px"></div>
    <h2 class="script" style="left:21px;top:12px;font-size:15px;font-weight:400">In our Hummus:</h2>
    <p class="body-copy" style="left:21px;top:30px;width:200px;font-size:10.3px;line-height:13.6px">We believe that our hummus doesn’t need all the extra ingredients like oils and preservatives. We want you to feel good after eating our products while also eating good food that is good for you! So we use fresh ingredients like lemon, garlic, red peppers, and sweet onions.</p>
    <h2 class="script" style="left:21px;top:136px;font-size:15px;font-weight:400">Ingredients:</h2>
    <p class="body-copy" style="left:21px;top:157px;width:295px;font-size:10.3px;line-height:13.6px">Organic Chickpeas, Organic Tahini, Organic Red Pepper, Sweet Onion, Garlic, Water, Lemon, Maple Syrup, Crushed Red Pepper, Pink Himalayan Salt, Cumin, Cayenne, Black Pepper, Baking Soda.</p>
    <div class="footer"><span class="web" style="font-size:14px">TheMarrowsNaturalFoods.com</span></div>
  </section>

  <!-- front label, large -->
  <section class="label front-large">
    <div class="pepper-photo" role="img" aria-label="Roasted red peppers on a white plate" style="left:229px;top:0;width:228px;height:243px"></div>
    <div class="brand-seal" style="left:47px;top:25px;width:190px;height:190px;font-size:24px">The Marrows</div>
    <div class="script" style="left:190px;top:220px;font-size:23px;transform:rotate(-3deg)">Made with real ingredients</div>
    <h1 class="product-name" style="left:43px;top:264px;font-size:38px">The Lark Hummus</h1>
    <p class="product-desc" style="left:48px;top:310px;width:380px;font-size:16.5px;line-height:18px">Roasted Red Pepper hummus infused with Crushed Red Pepper for a kick</p>
    <div class="band"></div>
    <div class="claim" style="left:28px;top:376px;width:80px"><svg width="46" height="46"><use href="#icon-oil-free"/></svg><span style="margin-top:6px">Oil free</span></div>
    <div class="claim" style="left:114px;top:376px;width:100px"><svg width="46" height="46"><use href="#icon-preservative-free"/></svg><span style="margin-top:6px">Preservative free</span></div>
    <div class="net-weight" style="right:30px;top:392px;font-size:14px;text-align:right">Net Wt.: <span style="font-size:22px">12 oz</span></div>
    <div class="web" style="right:30px;top:423px;font-size:12.5px">TheMarrowsNaturalFoods.com</div>
  </section>

</main>
</body>
</html>
```